Agriculture Business Card

I want to use my existing logo and use my tagline of "Don't Guess...Soil Test" on the card. Looking for a double sided card that will really get peoples attention.
Contact Info:
Marlow Field Crop Partners
Calvin Brusk
2716 K Lane
Otoe, NE 68592
402-555-0143
calvin.r.brusk@fieldmailbox.net

```html
<!DOCTYPE html>
<html lang="en">
<head>
<meta charset="utf-8">
<title>Marlow Field Crop Partners – Business Card</title>
<link rel="stylesheet" href="https://fonts.googleapis.com/css2?family=Fjalla+One&family=Arimo:wght@400&display=swap">
<style>
  :root {
    --page: #e9e9e9;
    --card: #2e2e2e;
    --white: #ffffff;
    --green: #2fa634;
    --gold: #f2b01e;
    --muted: #6a6a6a;
    --shade-light: #5a5a5a;
    --shade-dark: #262626;
  }
  * { margin: 0; padding: 0; box-sizing: border-box; }
  html, body { width: 1200px; height: 802px; overflow: hidden; }
  body {
    background: var(--page);
    font-family: "Arimo", Arial, sans-serif;
    position: relative;
  }
  .card {
    position: absolute;
    top: 246px;
    width: 540px;
    height: 309px;
    background: var(--card);
    box-shadow: 0 6px 18px rgba(0,0,0,0.18);
    overflow: hidden;
  }
  .card--front { left: 40px; }
  .card--back { left: 620px; }

  /* Front */
  .brand-mark {
    position: absolute;
    left: 150px;
    top: 70px;
    display: flex;
    align-items: center;
    gap: 12px;
  }
  .brand-mark__dot {
    width: 40px; height: 40px;
    border-radius: 50%;
    background: var(--gold);
  }
  .brand-mark__name {
    font-family: "Fjalla One", "Arial Narrow", sans-serif;
    font-size: 22px;
    line-height: 1.05;
    color: var(--white);
    width: 150px;
  }
  .holder-name {
    position: absolute;
    left: 34px;
    bottom: 48px;
    font-size: 27px;
    letter-spacing: 0.5px;
    color: var(--green);
    text-transform: uppercase;
  }
  .divider {
    position: absolute;
    left: 250px;
    top: 176px;
    width: 1px;
    height: 86px;
    background: var(--muted);
  }
  .contact {
    position: absolute;
    left: 266px;
    top: 180px;
    list-style: none;
    font-size: 13.5px;
    color: var(--white);
  }
  .contact li {
    display: flex;
    align-items: center;
    gap: 7px;
    height: 26px;
  }
  .contact svg { width: 12px; height: 12px; flex: none; }
  .contact .no-icon { padding-left: 19px; }

  /* Back */
  .back-emblem {
    position: absolute;
    left: 30px;
    top: 40px;
    width: 250px;
    height: 250px;
    border-radius: 30px;
    background: radial-gradient(circle at 55% 45%, var(--shade-light), var(--shade-dark) 72%);
    opacity: 0.85;
  }
  .back-title {
    position: absolute;
    right: 36px;
    top: 150px;
    text-align: right;
    font-family: "Fjalla One", "Arial Narrow", sans-serif;
    font-size: 30px;
    line-height: 1.05;
    color: var(--white);
  }
  .tagline {
    position: absolute;
    right: 36px;
    top: 232px;
    font-size: 16px;
    color: var(--gold);
  }
</style>
</head>
<body>

  <section class="card card--front" aria-label="Business card front">
    <div class="brand-mark">
      <span class="brand-mark__dot" aria-hidden="true"></span>
      <span class="brand-mark__name">Marlow Field Crop Partners</span>
    </div>

    <h1 class="holder-name">Calvin Brusk</h1>
    <span class="divider" aria-hidden="true"></span>

    <ul class="contact">
      <li>
        <svg viewBox="0 0 12 12" aria-hidden="true"><path fill="#2fa634" d="M2.4 1 4.3 3 3.4 4.4c.8 1.6 2.3 3.1 4 4l1.3-1L11 9.5 9.6 11C5.2 10.6 1.3 6.8 1 2.4z"/></svg>
        402-555-0143
      </li>
      <li>
        <svg viewBox="0 0 12 12" aria-hidden="true"><rect x="0.5" y="2" width="11" height="8" fill="#2fa634"/><path d="M1 2.6 6 6.6 11 2.6" stroke="#2e2e2e" stroke-width="1.2" fill="none"/></svg>
        calvin.r.brusk@fieldmailbox.net
      </li>
      <li class="no-icon">2716 K Lane, Otoe, NE 68592</li>
    </ul>
  </section>

  <section class="card card--back" aria-label="Business card back">
    <div class="back-emblem" role="img" aria-label="Large embossed emblem in dark grey tones"></div>
    <h2 class="back-title">Marlow Field Crop<br>Partners</h2>
    <p class="tagline">Don't Guess...Soil Test</p>
  </section>

</body>
</html>
```